Intuitive, look stunning website design for the street-level digital media platform that connects audiences with dynamic media on taxis and rideshare vehicles on BACK AND SIDE WINDOWS OF THE VEHICLE. SO FOOT TRAFFIC AND ALL OTHER TRAFFIC CAN SEE DISPLAY ON MOVING VEHICLE (in the future high glass building glass concept)
There should be 7 tabs VOLTANIX as home button, advertisers, partners, drivers, about us, news and contact.

Target Market(s)

The company works with taxi companies and rideshare drivers to install its proprietary advertising displays in their vehicles. These proprietary screens deliver dynamic content based on location-based, WiFi-enabled triggers.

Voltanix provides an additional revenue stream to maximize drive time and empowers brands to efficiently engage consumers across our nation's busiest cities, including San Francisco, Los Angeles, New York City, Dallas, Austin, Chicago and Miami.

Industry/Entity Type

Digital Marketing

Coding

Coded - Design and coding required

Number of Pages Required

5+ page

Font styles to use
Sans Serif

Requirements
Must have
• Use beautiful graphics and easy to read fonts.
Make sure graphics are compressed and optimized for fast loading.
Design should be consistent on brand throughout the website design.
Design an intuitive navigation system which allows users to get to the pages they need quickly.
Create pages that are standard for all business from small to big such; home, about us, product/services , sitemap ( seo purposes) contact us etc..
icons links for snapchat, instagram, client login, facbook
Nice to have
• Out of box concept
Should not have
• ITS NOT AN LCD BOX PLACED OVER THE CAR

```html
<!DOCTYPE html>
<html lang="en">
<head>
<meta charset="utf-8">
<title>Voltanix — Street-level digital media</title>
<link href="https://fonts.googleapis.com/css2?family=Poppins:wght@400;500;600;700;800&display=swap" rel="stylesheet">
<style>
:root{
  --black:#000;
  --blue:#1f7fc4;
  --blue-dark:#0b4d96;
  --navy:#13407e;
  --ink:#2a2a2a;
  --text:#444;
  --white:#fff;
  --grey-bg:#e4e6e8;
}
*{margin:0;padding:0;box-sizing:border-box}
html,body{width:1200px;height:3564px;overflow:hidden}
body{position:relative;font-family:'Poppins',sans-serif;color:var(--ink);background:var(--white)}
.abs{position:absolute}

/* header */
.site-header{position:absolute;left:0;top:0;width:1200px;height:130px;background:var(--black)}
.brand{position:absolute;left:160px;top:48px;display:flex;align-items:center;gap:10px;color:var(--white);font-weight:600;font-size:22px;letter-spacing:3px}
.brand .dot{width:26px;height:26px;border-radius:50%;background:var(--blue)}
.social{position:absolute;top:22px;display:flex;gap:10px;left:770px}
.social span{width:34px;height:34px;border-radius:50%;background:var(--white);display:block}
.client-login{position:absolute;left:902px;top:22px;width:124px;height:36px;border-radius:18px;background:var(--blue);color:var(--white);font-size:13px;font-weight:500;display:flex;align-items:center;justify-content:center}
.main-nav{position:absolute;top:80px;left:0;width:1200px;height:26px;font-size:15px;color:var(--white)}
.main-nav a{position:absolute;color:var(--white);text-decoration:none;transform:translateX(-50%);white-space:nowrap;line-height:26px}
.main-nav a.active{color:var(--blue);border:2px solid var(--blue);border-radius:16px;padding:0 12px;line-height:24px;top:-1px}

/* hero */
.hero{position:absolute;left:0;top:130px;width:1200px;height:630px;background:linear-gradient(180deg,#3a3d40 0%,#5b5a55 35%,#c99a2a 55%,#e2a91f 68%,#2d2c2b 85%,#6d6c6a 100%)}
.hero-title{position:absolute;top:386px;left:0;width:1200px;text-align:center;color:var(--white);font-size:96px;font-weight:800;letter-spacing:-1px}
.hero-curve{position:absolute;left:0;top:660px}
.dots{position:absolute;top:702px;left:574px;display:flex;gap:6px}
.dots span{width:8px;height:8px;border-radius:50%;background:var(--white)}

/* section titles */
.section-title{position:absolute;left:0;width:1200px;text-align:center;font-size:32px;font-weight:800;color:var(--ink);letter-spacing:-.5px}
.section-lead{position:absolute;text-align:center;font-size:13.5px;line-height:24px;color:var(--text)}

/* steps */
.step{position:absolute;width:240px;text-align:center}
.step-photo{position:absolute;width:208px;height:208px;border-radius:50%;border:3px solid var(--navy);padding:6px;background:var(--white)}
.step-photo div{width:100%;height:100%;border-radius:50%}
.step-num{position:absolute;width:66px;height:66px;border-radius:50%;background:var(--blue);border:4px solid var(--white);box-shadow:0 0 0 3px var(--navy);color:var(--white);font-weight:700;font-size:28px;display:flex;align-items:center;justify-content:center}
.step h3{font-size:20px;font-weight:600;margin-bottom:6px}
.step p{font-size:13.5px;line-height:22px;color:var(--text)}
.connector{position:absolute;top:1020px;height:8px;border-top:1px dotted #aaa;border-bottom:1px dotted #aaa}

/* about */
.about-title{position:absolute;left:172px;top:1444px;color:var(--white);font-size:34px;font-weight:800}
.about-text{position:absolute;left:172px;top:1502px;width:430px;color:var(--white);font-size:13.5px;line-height:24px}
.btn{position:absolute;left:172px;top:1732px;width:130px;height:44px;border-radius:22px;background:var(--blue);color:var(--white);font-size:13px;font-weight:700;display:flex;align-items:center;justify-content:center}

/* services */
.card{position:absolute;top:2054px;width:256px;height:360px;background:var(--white);box-shadow:0 2px 10px rgba(0,0,0,.12);text-align:center}
.card-photo{height:169px}
.card h3{font-size:19px;font-weight:500;margin:22px 0 10px}
.card p{font-size:12.5px;line-height:21px;color:var(--text);padding:0 26px}
.card .arrow{position:absolute;left:114px;bottom:22px}

/* cities */
.city{position:absolute;display:flex;align-items:center;justify-content:center;color:var(--white);font-size:17px;font-weight:600;text-shadow:0 1px 3px rgba(0,0,0,.6)}

/* footer */
.footer-brand{position:absolute;left:0;top:3330px;width:1200px;display:flex;justify-content:center;align-items:center;gap:12px;color:var(--white);font-size:30px;font-weight:600;letter-spacing:6px}
.footer-brand .dot{width:40px;height:40px;border-radius:50%;border:3px solid var(--white)}
.footer-nav{position:absolute;top:3456px;left:0;width:1200px;font-size:15px}
.footer-nav a{position:absolute;color:var(--white);text-decoration:none;transform:translateX(-50%)}
.copyright{position:absolute;top:3506px;left:0;width:1200px;text-align:center;color:var(--white);font-size:13px}
.page-code{position:absolute;top:3512px;left:1101px;color:var(--white);font-size:13px}
</style>
</head>
<body>

<header class="site-header">
  <div class="brand"><span class="dot"></span>VOLTANIX</div>
  <div class="social" aria-label="Social links">
    <span aria-label="Social link one"></span><span aria-label="Social link two"></span><span aria-label="Social link three"></span>
  </div>
  <div class="client-login">CLIENT LOGIN</div>
  <nav class="main-nav">
    <a class="active" style="left:388px">Home</a>
    <a style="left:494px">Advertisers</a>
    <a style="left:609px">Partners</a>
    <a style="left:709px">Drivers</a>
    <a style="left:811px">About us</a>
    <a style="left:907px">News</a>
    <a style="left:997px">Contact</a>
  </nav>
</header>

<section class="hero" role="img" aria-label="Yellow taxi with a rooftop display parked on a city street"></section>
<h1 class="hero-title">VOLTANIX</h1>
<svg class="hero-curve" width="1200" height="110" viewBox="0 0 1200 110">
  <path d="M0 22 Q600 150 1200 22 L1200 110 L0 110 Z" fill="#fff"/>
  <path d="M0 26 Q600 154 1200 26" fill="none" stroke="#1f7fc4" stroke-width="7"/>
</svg>
<div class="dots"><span></span><span></span><span></span><span></span></div>

<h2 class="section-title" style="top:832px">HOW IT WORKS</h2>
<div class="connector" style="left:382px;width:112px"></div>
<div class="connector" style="left:704px;width:114px"></div>

<div class="step-photo" style="left:173px;top:920px"><div role="img" aria-label="Hand holding a smartphone" style="background:linear-gradient(135deg,#e89a8a,#c0443a 60%,#f0d0c0)"></div></div>
<div class="step-photo" style="left:495px;top:920px"><div role="img" aria-label="Yellow taxi with roof display" style="background:linear-gradient(180deg,#3b3c3e,#e7b318 55%,#333)"></div></div>
<div class="step-photo" style="left:818px;top:920px"><div role="img" aria-label="Orange taxi with side advertising" style="background:linear-gradient(180deg,#5d6a5a,#e8632a 55%,#3a3a3a)"></div></div>
<div class="step-num" style="left:244px;top:1091px">01</div>
<div class="step-num" style="left:566px;top:1091px">02</div>
<div class="step-num" style="left:889px;top:1091px">03</div>

<div class="step" style="left:157px;top:1168px"><h3>Adilormloscn</h3><p>Lorem ipsum dolor sit ameto nsectetur adipiscing elit sed do eiusmod tempor idunt</p></div>
<div class="step" style="left:479px;top:1168px"><h3>Adilormloscn</h3><p>Lorem ipsum dolor sit ameto nsectetur adipiscing elit sed do eiusmod tempor idunt</p></div>
<div class="step" style="left:802px;top:1168px"><h3>Adilormloscn</h3><p>Lorem ipsum dolor sit ameto nsectetur adipiscing elit sed do eiusmod tempor idunt</p></div>

<div class="abs" role="img" aria-label="Grey city skyline backdrop" style="left:0;top:1860px;width:1200px;height:659px;background:linear-gradient(180deg,#f4f5f6 0%,#d9dbdd 40%,#c4c6c8 100%)"></div>

<svg class="abs" style="left:0;top:1320px" width="1200" height="580" viewBox="0 0 1200 580">
  <defs><linearGradient id="aboutGrad" x1="0" x2="1"><stop offset="0" stop-color="#0b4d96"/><stop offset="1" stop-color="#2383c4"/></linearGradient></defs>
  <path d="M0 71 Q600 -45 1200 71 L1200 500 Q600 640 0 500 Z" fill="url(#aboutGrad)"/>
  <circle cx="865" cy="278" r="155" fill="none" stroke="#fff" stroke-width="8"/>
  <circle cx="865" cy="278" r="143" fill="#d0643a"/>
</svg>
<div class="abs" role="img" aria-label="Orange taxi on a busy street" style="left:722px;top:1455px;width:286px;height:286px;border-radius:50%;background:linear-gradient(180deg,#6e7670,#e0642e 50%,#4a4c4e)"></div>

<h2 class="about-title">ABOUT VOLTANIX</h2>
<p class="about-text">Sed ut perspiciatis unde omnis iste natus error sit voluptate m accusantium doloremque laudantium, totam rem aperiam, eaque ipsa quae ab illo inventore veritatis et quasi architec to beatae vitae dicta sunt explicabo. Nemo enim ipsam volup ta tem quia voluptas sit asperSed ut perspiciatis unde omnis iste natus error sit voluptatem accusantium doloremque la udantium, totam rem aperiam, eaque ipsa quae ab illo inve ntore veritatis et quasi architecto beatae vitae dicta sunt explicabmo enim ipsam voluptat.</p>
<div class="btn">READ MORE</div>

<h2 class="section-title" style="top:1920px">WHAT WE DO</h2>
<p class="section-lead" style="left:390px;top:1980px;width:420px">Sed ut perspiciatis unde omnis iste natus error sit voluptate m accusantium doloremque laudantium, totariam</p>

<div class="card" style="left:172px"><div class="card-photo" role="img" aria-label="Yellow taxi outside an office building" style="background:linear-gradient(180deg,#3a3b3c,#e4b21c 65%,#555)"></div><h3>Finibuonorum</h3><p>Lorem ipsum dolor sit ame cons ectetur adipiscing elitsed do eius mod tempor incididunt ut labore et dolore malo</p><svg class="arrow" width="28" height="10"><path d="M0 5H26M21 1L26 5L21 9" stroke="#1f7fc4" stroke-width="1.5" fill="none"/></svg></div>
<div class="card" style="left:472px"><div class="card-photo" role="img" aria-label="Yellow taxi close-up" style="background:linear-gradient(180deg,#8a8a88,#e2a818 55%,#6b5a30)"></div><h3>Finibuonorum</h3><p>Lorem ipsum dolor sit ame cons ectetur adipiscing elitsed do eius mod tempor incididunt ut labore et dolore malo</p><svg class="arrow" width="28" height="10"><path d="M0 5H26M21 1L26 5L21 9" stroke="#1f7fc4" stroke-width="1.5" fill="none"/></svg></div>
<div class="card" style="left:770px"><div class="card-photo" role="img" aria-label="Taxis on a city street seen from above" style="background:linear-gradient(180deg,#9a9690,#5b5e5c 55%,#c9a62a 80%,#4f5250)"></div><h3>Finibuonorum</h3><p>Lorem ipsum dolor sit ame cons ectetur adipiscing elitsed do eius mod tempor incididunt ut labore et dolore malo</p><svg class="arrow" width="28" height="10"><path d="M0 5H26M21 1L26 5L21 9" stroke="#1f7fc4" stroke-width="1.5" fill="none"/></svg></div>

<h2 class="section-title" style="top:2625px">OUR NATION'S BUSIEST CITIES</h2>
<p class="section-lead" style="left:300px;top:2684px;width:600px">Sed ut perspiciatis unde omnis iste natus error sit voluptate accusantium doloremque laudantium, totam rem aperiam, eaque ipsa quae ab illo inventore veritatis et quasi architecto beatae vitae dicta sunt explicabo. Nemo enim ipsam volup</p>

<div class="city" role="img" aria-label="San Francisco skyline at sunset" style="left:172px;top:2773px;width:418px;height:138px;background:linear-gradient(180deg,#3c5a78,#a0684a 60%,#2b2f3a)">San Francisco</div>
<div class="city" role="img" aria-label="Los Angeles skyline" style="left:609px;top:2773px;width:199px;height:138px;background:linear-gradient(180deg,#6f7f95,#3d4250 60%,#8a4a3a)">Los Angeles</div>
<div class="city" role="img" aria-label="New York City skyline" style="left:828px;top:2773px;width:199px;height:138px;background:linear-gradient(180deg,#8a90a0,#6a5a4a 55%,#3a3a40)">New York City</div>
<div class="city" role="img" aria-label="Dallas skyline at dusk" style="left:172px;top:2927px;width:199px;height:137px;background:linear-gradient(180deg,#8a6aa0,#c0704a 55%,#3a3040)">Dallas</div>
<div class="city" role="img" aria-label="Austin skyline by the river" style="left:390px;top:2927px;width:200px;height:137px;background:linear-gradient(180deg,#2a3e78,#3a5a9a 55%,#1c2a50)">Austin</div>
<div class="city" role="img" aria-label="Chicago skyline at dusk" style="left:609px;top:2927px;width:199px;height:137px;background:linear-gradient(180deg,#5a6aa0,#3a4a7a 55%,#c07a4a)">Chicago</div>
<div class="city" role="img" aria-label="Miami towers" style="left:828px;top:2927px;width:199px;height:137px;background:linear-gradient(180deg,#6a9ac0,#405a7a 55%,#a07a5a)">Miami</div>

<div class="abs" role="img" aria-label="Light line-drawn city skyline" style="left:0;top:3080px;width:1200px;height:220px;background:linear-gradient(180deg,#fff,#eef1f4)"></div>

<svg class="abs" style="left:0;top:3250px" width="1200" height="314" viewBox="0 0 1200 314">
  <defs><linearGradient id="footGrad" x1="0" x2="1"><stop offset="0" stop-color="#0b4d96"/><stop offset="1" stop-color="#2383c4"/></linearGradient></defs>
  <path d="M0 50 Q600 -40 1200 50 L1200 314 L0 314 Z" fill="#1f7fc4"/>
  <path d="M0 72 Q600 -18 1200 72" fill="none" stroke="#fff" stroke-width="6"/>
  <path d="M0 80 Q600 -10 1200 80 L1200 314 L0 314 Z" fill="url(#footGrad)"/>
</svg>

<div class="footer-brand"><span class="dot"></span>VOLTANIX</div>
<nav class="footer-nav">
  <a style="left:291px">Home</a>
  <a style="left:398px">Advertisers</a>
  <a style="left:513px">Partners</a>
  <a style="left:613px">Drivers</a>
  <a style="left:714px">About us</a>
  <a style="left:810px">News</a>
  <a style="left:901px">Contact</a>
</nav>
<p class="copyright">© 2020 All rights are reserved. Privacy | Terms of use</p>
<span class="page-code">C4</span>

</body>
</html>
```